KSV Ledger Client Presentation

A concise power point presentation that follows the agenda of:
1. Hook- what is the pain you are solving (why even be on the call)
2. Short solution to hook --value proposition
3. Who you are
4. Detail of pain
5. Detail of solution
6. Economics /Benefit/ease to implement
7. Close/call to action
The graphics should include a lot of whitespace and a crisp, modern design.
I have this initial layout (see attached) and would like to have the designers AI it up to look much better. The graphics I have are terrible, we are in the hospital/medical space

```html
<!DOCTYPE html>
<html lang="en">
<head>
<meta charset="utf-8">
<title>KSV Ledger Client Presentation</title>
<link rel="stylesheet" href="https://fonts.googleapis.com/css2?family=Didact+Gothic&family=Cabin:wght@400;500&display=swap">
<style>
:root{
  --page:#ffffff;
  --ink:#1c1c1c;
  --muted:#444;
  --orange:#e8862c;
  --gold:#e4c26a;
  --amber:#d9803a;
  --sand:#c8b26a;
  --teal:#5e7a78;
  --steel:#6a8190;
  --sage:#8fa56c;
  --slate:#7f8a93;
  --rust:#b06a34;
}
*{box-sizing:border-box;margin:0;padding:0}
html,body{width:1200px;height:1200px;overflow:hidden;background:var(--page)}
body{position:relative;font-family:"Cabin",sans-serif;color:var(--ink)}
.slide{position:absolute;width:488px;height:274px;background:#fff;overflow:hidden;box-shadow:6px 8px 14px rgba(0,0,0,.28)}
.slide svg.art{position:absolute;inset:0;width:488px;height:274px}
.s1{left:89px;top:116px}
.s2{left:630px;top:350px}
.s3{left:89px;top:583px}
.s4{left:630px;top:817px}
.footer{position:absolute;top:261px;font-size:4.5px;letter-spacing:.2px;color:#555;text-transform:uppercase}
.footer.left{left:27px}
.footer.date{left:382px}
.footer.num{left:459px}
.title{font-family:"Didact Gothic",sans-serif;text-transform:uppercase;color:var(--ink);font-weight:400}

/* slide 1 */
.s1 .title{position:absolute;left:290px;top:72px;font-size:24px;letter-spacing:.3px}
.s1 .points{position:absolute;left:290px;top:112px;list-style:none;font-family:"Didact Gothic",sans-serif;font-size:13.5px;line-height:17px;text-transform:uppercase}
.s1 .points li{position:relative;padding-left:13px;margin-bottom:2px;width:160px}
.s1 .points li::before{content:"";position:absolute;left:0;top:6px;width:4px;height:4px;background:var(--ink)}

/* shared bullet list */
.dots{list-style:none}
.dots li{position:relative;padding-left:11px}
.dots li::before{content:"";position:absolute;left:0;width:2.5px;height:2.5px;background:var(--orange)}

/* slide 2 */
.s2 .title{position:absolute;left:27px;top:40px;font-size:13px}
.s2 .dots{position:absolute;left:27px;top:65px;width:135px;font-size:6px;line-height:8.4px}
.s2 .dots li{margin-bottom:8px}
.s2 .dots li.tight{margin-bottom:0}
.s2 .dots li::before{top:2.5px}
.s2 .node{fill-opacity:.9;stroke:#fff;stroke-width:1}
.s2 .node-label{font-family:"Didact Gothic",sans-serif;font-size:7px;fill:#fff;text-anchor:middle}
.s2 .core-label{font-family:"Didact Gothic",sans-serif;font-size:13px;fill:#fff;text-anchor:middle}

/* slide 3 */
.s3 .heading{position:absolute;left:27px;top:29px;font-family:"Didact Gothic",sans-serif;font-size:11.5px;line-height:15.3px}
.s3 .heading .title{display:block}
.s3 .letter{position:absolute;left:27px;top:149px;width:160px;font-size:8px;line-height:11px}

/* slide 4 */
.s4 .title{position:absolute;left:27px;top:38px;font-size:13px;line-height:17px}
.s4 .dots{position:absolute;left:27px;top:82px;width:120px;font-size:8px;line-height:11px}
.s4 .dots li{margin-bottom:3px}
.s4 .dots li::before{top:4px}
.s4 .risks{position:absolute;left:225px;top:49px;width:255px;color:#fff;font-size:5.5px;line-height:8px}
.s4 .risks h3{font-family:"Didact Gothic",sans-serif;font-weight:400;font-size:11px;text-transform:uppercase;margin-bottom:9px}
.s4 .risks h4{font-weight:400;font-size:7.5px;margin:6px 0 8px}
.s4 .risks .who{text-decoration:underline;margin-top:6px}
.s4 .risks ul{list-style:none}
.s4 .risks li{position:relative;padding-left:11px}
.s4 .risks li::before{content:"";position:absolute;left:1px;top:3px;width:2px;height:2px;border-radius:50%;background:#fff}
.s4 .footer{color:#fff}
.s4 .footer.left{color:#555}
</style>
</head>
<body>

<section class="slide s1">
  <svg class="art" viewBox="0 0 488 274">
    <defs>
      <linearGradient id="wood" x1="0" y1="0" x2="1" y2="1">
        <stop offset="0" stop-color="#8a6d58"/><stop offset=".45" stop-color="#c98a4a"/><stop offset="1" stop-color="#a8682f"/>
      </linearGradient>
    </defs>
    <path d="M0 0H232C278 70 276 200 226 274H0Z" fill="var(--gold)"/>
    <path d="M0 0H222C268 70 266 200 218 274H0Z" fill="var(--orange)"/>
    <path d="M0 0H211C256 70 256 200 211 274H0Z" fill="url(#wood)" role="img" aria-label="Photo of a hand tapping a phone on a card payment terminal over a wooden table"/>
  </svg>
  <h1 class="title">VeilPay™</h1>
  <ul class="points">
    <li>Payment Privacy</li>
    <li>Compliance</li>
    <li>Cost Management Solution</li>
  </ul>
  <span class="footer left">KSV Ledger Client Presentation</span>
  <span class="footer date">December 2024</span>
  <span class="footer num">1</span>
</section>

<section class="slide s2">
  <svg class="art" viewBox="0 0 488 274">
    <defs>
      <linearGradient id="desk" x1="0" y1="0" x2="1" y2="1">
        <stop offset="0" stop-color="#e6ebe4"/><stop offset=".5" stop-color="#f2f3f1"/><stop offset="1" stop-color="#e9ebec"/>
      </linearGradient>
    </defs>
    <rect width="488" height="274" fill="url(#desk)" role="img" aria-label="Faded photo of a stethoscope and medical forms on a desk"/>
    <circle class="node" cx="319" cy="57" r="40" fill="var(--sand)"/>
    <circle class="node" cx="242" cy="115" r="40" fill="var(--teal)"/>
    <circle class="node" cx="398" cy="115" r="40" fill="var(--steel)"/>
    <circle class="node" cx="272" cy="206" r="40" fill="var(--sage)"/>
    <circle class="node" cx="368" cy="206" r="40" fill="var(--slate)"/>
    <circle cx="319" cy="142" r="62" fill="var(--amber)" fill-opacity=".88" stroke="#fff" stroke-width="1"/>
    <text class="node-label" x="319" y="54">Truly</text>
    <text class="node-label" x="319" y="66">Private</text>
    <text class="node-label" x="237" y="113">Useless to</text>
    <text class="node-label" x="237" y="122">Hackers</text>
    <text class="node-label" x="404" y="113">Data is DE-</text>
    <text class="node-label" x="404" y="122">IDENTIFIED</text>
    <text class="node-label" x="271" y="208">No use to 3rd Party</text>
    <text class="node-label" x="271" y="217">Marketers and List</text>
    <text class="node-label" x="271" y="226">Brokers.</text>
    <text class="node-label" x="374" y="204">Impossible</text>
    <text class="node-label" x="374" y="213">to view</text>
    <text class="core-label" x="319" y="147">VEILPAY™</text>
  </svg>
  <h2 class="title">Why VeilPay™</h2>
  <ul class="dots">
    <li>All your bank needs to approve your purchase is your name the amount your charging.</li>
    <li>Current PCI / DSS protocols, however, send much more data through Crestline / Northpay / Orbis</li>
    <li class="tight">Provider name and location</li>
    <li>What the charge was for (Procedure, Supplies, Medicines)</li>
    <li>They SELL THAT DATA.</li>
    <li>Marketers, List Providers, ANY 3rd party can buy your data.</li>
    <li>And Hackers would gain access to it in a data breach.</li>
  </ul>
  <span class="footer left">KSV Ledger Client Presentation</span>
  <span class="footer date">December 2024</span>
  <span class="footer num">2</span>
</section>

<section class="slide s3">
  <svg class="art" viewBox="0 0 488 274">
    <defs>
      <linearGradient id="clinic" x1="0" y1="0" x2="1" y2="1">
        <stop offset="0" stop-color="#e9e4dc"/><stop offset=".5" stop-color="#f4f4f2"/><stop offset="1" stop-color="#8fb4d8"/>
      </linearGradient>
    </defs>
    <path d="M206 0C166 90 176 200 270 274H488V0Z" fill="var(--gold)"/>
    <path d="M214 0C176 92 186 200 280 274H488V0Z" fill="var(--orange)"/>
    <path d="M222 0C186 94 196 200 290 274H488V0Z" fill="url(#clinic)" role="img" aria-label="Photo of a patient paying by card on a handheld terminal at a clinic desk"/>
  </svg>
  <div class="heading">
    <span class="title">How private are</span>
    <span class="title">credit card</span>
    <span class="title">transactions?</span>
    <span>Like A:</span><br>
    <span>- Post-card</span><br>
    <span>- E-mail Blast</span><br>
    <span>- TV Commercial</span>
  </div>
  <p class="letter">Hello 3rd Party Vendors, List Brokers and Hackers,<br>This is Danas Crestline Card, its January 7, 2025 and I am<br>spending $562 at Desert Bloom Women's Clinic in Phoenix Arizona .<br>Thought you would like to know!<br>Best wishes, Northpay</p>
  <span class="footer left">KSV Ledger Client Presentation</span>
  <span class="footer date">December 2024</span>
</section>

<section class="slide s4">
  <svg class="art" viewBox="0 0 488 274">
    <defs>
      <linearGradient id="hacker" x1="0" y1="0" x2="1" y2="1">
        <stop offset="0" stop-color="#c07a3e"/><stop offset=".55" stop-color="#a8622f"/><stop offset="1" stop-color="#b8703a"/>
      </linearGradient>
    </defs>
    <path d="M214 0C160 80 160 200 232 274H488V0Z" fill="var(--gold)"/>
    <path d="M222 0C170 80 170 200 240 274H488V0Z" fill="var(--orange)"/>
    <path d="M230 0C180 80 180 200 250 274H488V0Z" fill="url(#hacker)" role="img" aria-label="Orange-tinted photo of a hooded figure at a laptop with code in the background"/>
  </svg>
  <h2 class="title">Credit card<br>transactions</h2>
  <ul class="dots">
    <li>Not Private</li>
    <li>Patient and provider names disclosed at risk across the payment chain:</li>
    <li>List Vendors</li>
    <li>3rd Party Marketers</li>
    <li>Hackers</li>
    <li>HIPPA/Cures Act/State privacy and consent liability</li>
    <li>Expensive 3% of total transaction paid by provider</li>
  </ul>
  <div class="risks">
    <h3>Risks to both provider and patient</h3>
    <h4>BEFORE VeilPay:</h4>
    <p class="who">Provider Risk:</p>
    <ul>
      <li>Exposed to Litigation from Data Breach</li>
      <li>Exposed to Enforcement Risk from HHS for HIPAA and Cures Violations</li>
    </ul>
    <p class="who">Patient Risk:</p>
    <ul><li>Exposed to privacy breaches for every transaction</li></ul>
    <h4>AFTER VeilPay:</h4>
    <p class="who">Provider:</p>
    <ul>
      <li>All transactional data is de-identified except the name and amount.</li>
      <li>Provider does not reveal PHI, so data cannot be stolen or sold.</li>
    </ul>
    <p class="who">Patient:</p>
    <ul><li>Personal Health Information remains private and is unreadable.</li></ul>
  </div>
  <span class="footer left">KSV Ledger Client Presentation</span>
  <span class="footer date">December 2024</span>
  <span class="footer num">4</span>
</section>

</body>
</html>
```